依頼詳細
レストラン、学校給食センター、病院等で使用する食材を運んでいるトラック車両の荷台両側面へプリント。
運送会社としてアピールするための、食品を安全に運送しているイメージデザイン案希望。
それに合ったキャッチフレーズも入れて頂ければと思います。
詳しいサイズ等は記載項目を参照してください。
記載項目
サイズはデザインのピクセル数で掲載しております。

縦 4,600pixel × 横 8,400pixel 以上で作成が希望ですが、
最低条件、縦横4,000pixel以上あれば幸いです。
希望イメージ
• +5 0 +5
• シンプル
複雑
• 単色
カラフル
• 暗い
明るい
• 日常
高級
• 遊び心
厳粛
• 未来的
伝統的
• 女性的
男性的
希望する色
納品ファイル
• 高解像度JPG (.jpg)
• イラストレーター形式 (.ai)
• フォトショップ形式 (.psd)
補足説明
ご質問等があればお申し付けください。

```html
<!DOCTYPE html>
<html lang="ja">
<head>
<meta charset="UTF-8">
<title>みんなのおいしいと安全をお届けします！</title>
<link rel="stylesheet" href="https://fonts.googleapis.com/css2?family=Yomogi&display=swap">
<style>
  :root {
    --canvas-bg: #ffffff;
    --sky-top: #8ad8f2;
    --sky-bottom: #f1fafc;
    --produce-warm: #d98a4a;
    --produce-green: #6f9a3c;
    --produce-light: #e9d9a8;
    --stripe-blue: #5aa8e6;
    --band-yellow: #fff23a;
    --band-pale: #fffbb0;
    --ink: #1f1f1f;
    --mascot-tone: #f2f6e8;
  }
  html, body {
    margin: 0;
    padding: 0;
    width: 1200px;
    height: 661px;
    overflow: hidden;
    background: var(--canvas-bg);
  }
  .panel {
    position: relative;
    width: 1200px;
    height: 661px;
  }
  .panel-art {
    position: absolute;
    inset: 0;
    width: 1200px;
    height: 661px;
  }
  .catchphrase {
    position: absolute;
    left: 578px;
    top: 176px;
    margin: 0;
    font-family: "Yomogi", cursive;
    font-weight: 400;
    color: var(--ink);
    font-size: 66px;
    line-height: 92px;
    letter-spacing: 2px;
  }
  .catchphrase .line { display: block; white-space: nowrap; }
  .catchphrase .line-2 { padding-left: 70px; }
  .catchphrase .line-3 { padding-left: 70px; }
  .catchphrase .line-4 { padding-left: 70px; }
</style>
</head>
<body>
  <main class="panel">
    <svg class="panel-art" viewBox="0 0 1200 661" xmlns="http://www.w3.org/2000/svg">
      <defs>
        <linearGradient id="sky-gradient" x1="0" y1="0" x2="0" y2="1">
          <stop offset="0" stop-color="var(--sky-top)"/>
          <stop offset="1" stop-color="var(--sky-bottom)"/>
        </linearGradient>
        <linearGradient id="produce-gradient" x1="0" y1="0" x2="1" y2="1">
          <stop offset="0" stop-color="var(--produce-warm)"/>
          <stop offset="0.45" stop-color="var(--produce-green)"/>
          <stop offset="1" stop-color="var(--produce-light)"/>
        </linearGradient>
        <linearGradient id="band-gradient" x1="0" y1="0" x2="1" y2="0">
          <stop offset="0" stop-color="var(--band-yellow)"/>
          <stop offset="0.7" stop-color="var(--band-yellow)"/>
          <stop offset="1" stop-color="var(--band-pale)"/>
        </linearGradient>
        <clipPath id="arch-clip">
          <path d="M40,600 C40,210 300,22 600,22 C900,22 1160,210 1160,560 L1160,640 L40,640 Z"/>
        </clipPath>
      </defs>

      <g clip-path="url(#arch-clip)">
        <rect class="sky" x="0" y="0" width="1200" height="661" fill="url(#sky-gradient)"/>

        <rect class="produce-photo" x="195" y="262" width="500" height="284"
              fill="url(#produce-gradient)" role="img"
              aria-label="色とりどりの新鮮な野菜の写真（トマト、カリフラワー、ブロッコリー、パプリカ、じゃがいも、とうもろこし）"/>

        <path class="band-yellow" d="M30,560 C300,548 700,540 1170,500 L1170,560 C900,610 500,650 30,661 Z"
              fill="url(#band-gradient)"/>
        <path class="stripe-blue" d="M30,548 C320,540 720,532 1170,490 L1170,502 C720,546 320,556 30,562 Z"
              fill="var(--stripe-blue)"/>
      </g>

      <rect class="mascots" x="990" y="322" width="130" height="112" rx="56"
            fill="var(--mascot-tone)" role="img"
            aria-label="笑顔の二人組マスコットキャラクター（緑と赤の丸いキャラクター）"/>
    </svg>

    <h1 class="catchphrase">
      <span class="line line-1">みんなの</span>
      <span class="line line-2">おいしいと</span>
      <span class="line line-3">安全を</span>
      <span class="line line-4">お届けします！</span>
    </h1>
  </main>
</body>
</html>
```